Computer consultant business card

Brimlo Software is a newly started computer consulting company. It's a small one-man company that provides mostly Velunix applications but also websites in collaboration with designers. I'm running this company on the side of full time university studies.

I want the final design to be clean and memorable. Be creative! :)

Some inspiration:
http://www.tavelpix.net/design/73519
http://www.tavelpix.net/design/2739566/business-card-design-by-quillbop
http://www.tavelpix.net/design/804613/business-card-design-by-lorvena-brukwaldsen

See attachment for my company logo.
Updates

I would like to thank everyone for submitting! I'll need a couple of days to review and ultimately select a design.

Target Market(s)

Non-technical entrepreneurs and small companies.

Industry/Entity Type

University

Requirements
Must have
• My company logo.
In any way, both colors from my logo.
First- and last name, e-mail and phone number.
Double-sided design.
Nice to have
• Something creative with the symbol in my logo

```html
<!DOCTYPE html>
<html lang="en">
<head>
<meta charset="utf-8">
<title>Brimlo Software — Business Card</title>
<link rel="stylesheet" href="https://fonts.googleapis.com/css2?family=Open+Sans:wght@400;700&family=Varela+Round&display=swap">
<style>
  :root {
    --brand-blue: #3b66ac;
    --brand-blue-deep: #2f5797;
    --brand-blue-soft: #4673ba;
    --ink: #2a2a2a;
    --ink-soft: #3a3a3a;
    --paper: #ffffff;
    --panel-grey: #e2e2e2;
    --panel-lilac: #e7eaf6;
    --stage: #ececec;
  }
  * { box-sizing: border-box; margin: 0; padding: 0; }
  html, body { width: 1200px; height: 1016px; overflow: hidden; }
  body {
    background: var(--stage);
    font-family: "Open Sans", Arial, sans-serif;
    position: relative;
  }
  .card {
    position: absolute;
    left: 290px;
    width: 620px;
    height: 354px;
    border-radius: 4px;
    overflow: hidden;
    box-shadow: 0 6px 18px rgba(0,0,0,0.18);
  }

  /* Front side */
  .card-front {
    top: 90px;
    background: radial-gradient(circle at 55% 45%, var(--brand-blue-soft) 0%, var(--brand-blue) 45%, var(--brand-blue-deep) 100%);
    display: flex;
    align-items: center;
    justify-content: center;
  }
  .front-wordmark {
    display: flex;
    align-items: center;
    gap: 20px;
    color: var(--paper);
  }
  .wordmark-dot {
    width: 62px; height: 62px;
    border-radius: 50%;
    background: var(--paper);
  }
  .wordmark-name {
    font-family: "Varela Round", "Open Sans", sans-serif;
    font-size: 78px;
    line-height: 1;
    letter-spacing: 1px;
  }

  /* Back side */
  .card-back {
    top: 540px;
    background: var(--paper);
  }
  .back-panel {
    position: absolute;
    right: 0; top: 0;
    width: 260px; height: 270px;
    background: linear-gradient(180deg, var(--panel-grey) 0%, var(--panel-grey) 55%, var(--panel-lilac) 55%, var(--panel-lilac) 100%);
  }
  .back-wordmark {
    position: absolute;
    left: 46px; top: 42px;
    display: flex; align-items: center; gap: 16px;
    color: var(--ink);
  }
  .back-wordmark .wordmark-dot {
    width: 48px; height: 48px;
    background: var(--brand-blue);
  }
  .back-wordmark .wordmark-name { font-size: 60px; color: var(--ink); }

  .edge-tab {
    position: absolute;
    left: 0; top: 188px;
    width: 16px; height: 56px;
    background: var(--brand-blue);
  }
  .identity {
    position: absolute;
    left: 52px; top: 150px;
  }
  .person-name {
    font-weight: 700;
    font-size: 22px;
    color: var(--brand-blue);
    letter-spacing: 0.5px;
  }
  .person-role {
    font-size: 18px;
    color: var(--ink-soft);
    margin-top: -2px;
  }
  .contacts {
    list-style: none;
    margin-top: 22px;
    font-size: 16px;
    color: var(--ink);
  }
  .contacts li { display: flex; align-items: center; gap: 8px; line-height: 1.45; }
  .contacts svg { width: 12px; height: 12px; flex: none; }

  .band-blue {
    position: absolute;
    left: 0; right: 0; bottom: 30px;
    height: 10px;
    background: var(--brand-blue);
  }
  .band-dark {
    position: absolute;
    left: 0; right: 0; bottom: 0;
    height: 30px;
    background: var(--ink);
  }
  .band-dark-tab {
    position: absolute;
    right: 0; bottom: 40px;
    width: 250px; height: 46px;
    background: var(--ink);
    border-top-left-radius: 22px;
  }
  .band-blue-tab {
    position: absolute;
    right: 0; bottom: 86px;
    width: 260px; height: 8px;
    background: var(--brand-blue);
    border-top-left-radius: 8px;
  }
</style>
</head>
<body>

  <section class="card card-front" aria-label="Business card front">
    <div class="front-wordmark">
      <span class="wordmark-dot" aria-hidden="true"></span>
      <span class="wordmark-name">brimlo</span>
    </div>
  </section>

  <section class="card card-back" aria-label="Business card back">
    <div class="back-panel" aria-hidden="true"></div>

    <div class="back-wordmark">
      <span class="wordmark-dot" aria-hidden="true"></span>
      <span class="wordmark-name">brimlo</span>
    </div>

    <div class="edge-tab" aria-hidden="true"></div>

    <div class="identity">
      <p class="person-name">YOUR NAME</p>
      <p class="person-role">Job Title</p>
      <ul class="contacts">
        <li>
          <svg viewBox="0 0 12 12" aria-hidden="true"><rect x="3" y="0.5" width="6" height="11" rx="1.2" fill="none" stroke="var(--brand-blue)" stroke-width="1.2"/><circle cx="6" cy="9.5" r="0.7" fill="var(--brand-blue)"/></svg>
          000-000-000
        </li>
        <li>
          <svg viewBox="0 0 12 12" aria-hidden="true"><rect x="0.5" y="2.5" width="11" height="7" fill="var(--brand-blue)"/><path d="M0.5 2.5 L6 6.5 L11.5 2.5" fill="none" stroke="#fff" stroke-width="1"/></svg>
          name@domainname.com
        </li>
      </ul>
    </div>

    <div class="band-blue-tab" aria-hidden="true"></div>
    <div class="band-dark-tab" aria-hidden="true"></div>
    <div class="band-blue" aria-hidden="true"></div>
    <div class="band-dark" aria-hidden="true"></div>
  </section>

</body>
</html>
```